Brochure 2 fold and Trifold

We need 2 types of brochure (2 fold and Trifold) design for our Brand "VELOURA BRIGHT" Logo (La douceur de Sorène) is in rose gold color
Target Market(s)
Women ages 17 and up
Industry/Entity Type
Supplement
Font styles to use
Serif
Script
Requirements
Must have
- Rose gold color tone make it look premium, minimalist look

```html
<!DOCTYPE html>
<html lang="en">
<head>
<meta charset="utf-8">
<title>Veloura Bright Brochure</title>
<link rel="stylesheet" href="https://fonts.googleapis.com/css2?family=Montserrat:wght@300;400;600;700&family=Cormorant+Garamond:wght@500&display=swap">
<style>
:root{
  --stage:#2f2f2f;
  --paper:#ffffff;
  --rose:#d49a98;
  --rose-deep:#c98583;
  --rose-band:#e9b9b8;
  --rose-panel:#d9a3a1;
  --ink:#1c1c1c;
  --grey:#a3a3a3;
  --grey-dark:#7c7c7c;
  --sans:'Montserrat', Arial, sans-serif;
  --serif:'Cormorant Garamond', Georgia, serif;
}
*{box-sizing:border-box;margin:0;padding:0}
html,body{width:1060px;height:1200px;overflow:hidden;background:var(--stage);font-family:var(--sans);color:var(--ink)}
.spread{position:absolute;left:60px;width:940px;height:540px;display:flex;box-shadow:0 10px 30px rgba(0,0,0,.45)}
.spread--covers{top:30px}
.spread--inside{top:630px}
.page{position:relative;width:470px;height:540px;background:var(--paper);overflow:hidden}
.page + .page{border-left:1px solid #e4e4e4}
.band{position:absolute;left:0;right:0;bottom:0;height:34px;background:var(--rose-band)}
.placeholder{position:absolute}
.wordmark{font-family:var(--serif);font-weight:500;color:var(--rose);letter-spacing:.35em;text-align:center}
.title{font-family:var(--sans);font-weight:400;letter-spacing:.04em}
.title .rose{color:var(--rose)}

/* back cover */
.back .tagline{position:absolute;left:40px;top:34px;font-size:14px;color:var(--rose)}
.back .allinone{position:absolute;left:150px;top:54px;font-size:22px;letter-spacing:.05em}
.back .fern-faint{left:0;top:70px;width:120px;height:230px;background:linear-gradient(160deg,#f2f2f2,#e6e6e6)}
.back .capsules{left:136px;top:86px;width:200px;height:120px;background:linear-gradient(135deg,#cfe6df,#5f9f8f 60%,#a9d2c7)}
.back .title{position:absolute;left:100px;top:218px;font-size:28px}
.back .sub{position:absolute;left:168px;top:254px;font-size:11px}
.back .distrib{position:absolute;left:250px;top:280px;font-size:11px}
.back .dbox{position:absolute;left:220px;top:298px;width:200px;height:100px;border:1px solid #9a9a9a}
.back .portrait{left:0;top:330px;width:230px;height:176px;background:linear-gradient(120deg,#f3ddd2,#e9c3b3 55%,#fbf4f0)}
.back .wordmark{position:absolute;left:70px;top:446px;width:140px}
.back .wordmark small{display:block;font-size:8px;letter-spacing:.3em}
.back .wordmark span{font-size:22px}
.back .call{position:absolute;left:268px;top:410px;font-size:13px;letter-spacing:.06em}
.back .phone{position:absolute;left:262px;top:426px;font-size:22px;letter-spacing:.04em}
.back .web{position:absolute;left:266px;top:456px;font-size:11px}

/* front cover */
.front .wordmark{position:absolute;left:0;right:0;top:46px}
.front .wordmark small{display:block;font-size:9px}
.front .wordmark span{font-size:28px}
.front .hero{left:140px;top:120px;width:200px;height:150px;background:radial-gradient(circle at 70% 70%,#f7f7f7 0 28%,transparent 30%),linear-gradient(140deg,#5aa13a,#2f7a24 45%,#eeeeee 46%)}
.front .title{position:absolute;left:0;right:0;top:290px;text-align:center;font-size:28px}
.front .rule{position:absolute;left:185px;width:100px;height:1px;background:var(--rose)}
.front .desc{position:absolute;left:0;right:0;top:348px;text-align:center;font-size:13px;line-height:1.35}

/* inside left */
.panel{position:absolute;left:0;top:0;bottom:0;width:235px;background:linear-gradient(180deg,var(--rose-panel),#e7bdbb);color:#fff;padding:40px 20px 0 26px}
.panel h2{font-size:15px;font-weight:700;line-height:1.15;letter-spacing:.03em}
.panel h3{font-size:9.5px;font-weight:700;letter-spacing:.05em;margin-bottom:12px}
.panel h4{display:inline-block;border:1px solid #fff;border-radius:10px;padding:1px 8px;font-size:11px;font-weight:600;margin:6px 0 4px}
.panel p{font-size:9px;line-height:1.3;margin-bottom:8px}
.panel .wordmark{position:absolute;left:0;right:0;bottom:44px;color:#f4d6d4}
.panel .wordmark small{display:block;font-size:8px}
.panel .wordmark span{font-size:26px}
.inside-left .portrait{left:235px;top:0;width:235px;height:300px;background:linear-gradient(160deg,#8a6a58 0 22%,#f5e2d8 40%,#f9efe9)}
.inside-left .still{left:290px;top:330px;width:180px;height:150px;background:radial-gradient(circle at 70% 75%,#f7f7f7 0 26%,transparent 28%),linear-gradient(140deg,#5aa13a,#2f7a24 45%,#ffffff 46%)}

/* inside right */
.benefits-head{position:absolute;left:30px;top:70px}
.benefits-head .lead{font-size:16px}
.benefits-head .name{font-size:22px;color:var(--rose);line-height:1.05;letter-spacing:.03em}
.benefit-list{position:absolute;left:230px;top:24px;width:214px;background:var(--grey);border-radius:12px;padding:14px 14px;list-style:none;color:#fff}
.benefit-list li{font-size:8px;font-weight:700;letter-spacing:.05em;margin:5px 0;padding-left:10px;position:relative;line-height:1.2}
.benefit-list li::before{content:"";position:absolute;left:0;top:2px;width:5px;height:5px;border-radius:50%;background:var(--rose)}
.chart-main{position:absolute;left:60px;top:170px}
.chart-title{position:absolute;left:110px;top:156px;font-size:8px}
.caption{position:absolute;left:100px;top:296px;font-size:7px;color:#fff;background:var(--rose);padding:2px 6px}
.study{position:absolute;left:60px;top:318px;width:360px;font-size:10px;line-height:1.3}
.chart-melasma{position:absolute;left:30px;top:360px}
.stat{position:absolute;left:150px;top:368px;font-size:10px;text-align:center}
.study-2{position:absolute;left:268px;top:420px;width:180px;font-size:10px;line-height:1.3}
</style>
</head>
<body>

<section class="spread spread--covers">
  <article class="page back">
    <div class="placeholder fern-faint" role="img" aria-label="Faint fern leaf decoration"></div>
    <p class="tagline">One of the first Skin &amp; Sun Protection</p>
    <p class="allinone">ALL IN ONE</p>
    <div class="placeholder capsules" role="img" aria-label="Clear supplement capsules on teal"></div>
    <h1 class="title"><span class="rose">VELOURA</span> BRIGHT</h1>
    <p class="sub">Nature's solution to skin whitening</p>
    <p class="distrib">Distributed by:</p>
    <div class="dbox"></div>
    <div class="placeholder portrait" role="img" aria-label="Portrait of a woman touching her face"></div>
    <div class="wordmark"><small>LA DOUCEUR DE</small><span>SORÈNE</span></div>
    <p class="call">CALL US TODAY</p>
    <p class="phone">1234567890</p>
    <p class="web">www.velourabright.example</p>
    <div class="band"></div>
  </article>

  <article class="page front">
    <div class="wordmark"><small>LA DOUCEUR DE</small><span>SORÈNE</span></div>
    <div class="placeholder hero" role="img" aria-label="Fern frond with white tomatoes"></div>
    <div class="rule" style="top:282px"></div>
    <h1 class="title"><span class="rose">VELOURA</span> BRIGHT</h1>
    <div class="rule" style="top:332px"></div>
    <p class="desc">Skin Whitening &amp; Sun Protection all in one<br>Oral supplements</p>
    <div class="band"></div>
  </article>
</section>

<section class="spread spread--inside">
  <article class="page inside-left">
    <div class="panel">
      <h2>SKIN WHITENING &amp;<br>SUN PROTECTION:</h2>
      <h3>THE SCIENTIFIC ANSWER</h3>
      <h4>1) LumiCarot</h4>
      <p>An award winning natural supplement using non-GMO tomato species rich in colourless carotenoids, phytoene and phytofluene. This patented combination provides superior whitening, UVA and UVB protection, anti-inflammatory and antioxidant properties.</p>
      <h4>2) Polypodium leucotomos</h4>
      <p>Naturally extracted from a tropical natural fern found in the Americas. It has been used for centuries by the natives for its superior benefits. Now clinically proven to protect against UV radiation due to its antioxidant, anti-inflammatory and DNA repair abilities.</p>
      <h4>3) L-Cysteine</h4>
      <p>A potent amino acid that has very high skin-whitening abilities. It prevents the production of pigment cells when the skin is exposed to UV rays and stimulates the production of Glutathione, another strong skin-whitening antioxidant.</p>
      <div class="wordmark"><small>LA DOUCEUR DE</small><span>SORÈNE</span></div>
    </div>
    <div class="placeholder portrait" role="img" aria-label="Portrait of a smiling woman with eyes closed"></div>
    <div class="placeholder still" role="img" aria-label="Fern frond with white tomatoes"></div>
  </article>

  <article class="page inside-right">
    <div class="benefits-head">
      <p class="lead">Benefits of</p>
      <p class="name">VELOURA<br>BRIGHT</p>
    </div>
    <ul class="benefit-list">
      <li>SKIN WHITENING</li>
      <li>COLLAGEN PROTECTION</li>
      <li>DNA REPAIR</li>
      <li>PREVENTS AGAINST PREMATURE SKIN AGING</li>
      <li>ENHANCED ANTIOXIDANT &amp; ANTI-INFLAMMATORY EFFECTS</li>
      <li>NATURAL UV PROTECTION</li>
    </ul>

    <p class="chart-title">Average Clinical improvement of skin parameters</p>
    <svg class="chart-main" width="300" height="124" viewBox="0 0 300 124" aria-label="Bar chart of skin improvement at day 42 and day 84">
      <line x1="20" y1="10" x2="20" y2="100" stroke="#999" stroke-width="1"/>
      <line x1="20" y1="100" x2="230" y2="100" stroke="#999" stroke-width="1"/>
      <g fill="#d49a98">
        <rect x="32" y="70" width="12" height="30"/><rect x="72" y="52" width="12" height="48"/>
        <rect x="112" y="56" width="12" height="44"/><rect x="152" y="78" width="12" height="22"/>
        <rect x="192" y="82" width="12" height="18"/>
      </g>
      <g fill="#8f8f8f">
        <rect x="46" y="48" width="12" height="52"/><rect x="86" y="34" width="12" height="66"/>
        <rect x="126" y="46" width="12" height="54"/><rect x="166" y="66" width="12" height="34"/>
        <rect x="206" y="60" width="12" height="40"/>
      </g>
      <g font-family="Montserrat, sans-serif" font-size="6" fill="#555">
        <text x="36" y="110">Tone</text><text x="72" y="110">Texture</text><text x="114" y="110">Clarity</text>
        <text x="152" y="110">Firmness</text><text x="192" y="110">Evenness</text>
      </g>
      <rect x="240" y="14" width="6" height="5" fill="#d49a98"/><text x="250" y="19" font-family="Montserrat, sans-serif" font-size="7">Day 42</text>
      <rect x="240" y="24" width="6" height="5" fill="#8f8f8f"/><text x="250" y="29" font-family="Montserrat, sans-serif" font-size="7">Day 84</text>
    </svg>
    <p class="caption">Figure 1: Graphic representation of the average changes in clinical scoring</p>
    <p class="study">Skin improvement results of a clinical study conducted by dermatologists measuring skin quality after 12 weeks use of colourless carotenoids (Skin Science Review 2015; 2(4) Page178-182)</p>

    <p class="stat">-42.1%<br>p&lt;0.05</p>
    <svg class="chart-melasma" width="220" height="140" viewBox="0 0 220 140" aria-label="Bar chart of melasma intensity reduction">
      <line x1="30" y1="20" x2="30" y2="130" stroke="#555" stroke-width="1"/>
      <line x1="30" y1="130" x2="200" y2="130" stroke="#555" stroke-width="1"/>
      <g font-family="Montserrat, sans-serif" font-size="9" fill="#333">
        <text x="16" y="133">0</text><text x="16" y="113">2</text><text x="16" y="88">4</text><text x="16" y="63">6</text>
      </g>
      <rect x="54" y="48" width="40" height="82" fill="#d49a98" stroke="#555" stroke-width="1"/>
      <rect x="94" y="60" width="40" height="70" fill="#a3a3a3" stroke="#555" stroke-width="1"/>
      <path d="M74 40 H114 V52" fill="none" stroke="#222" stroke-width="1.5"/>
      <path d="M109 48 L114 55 L119 48" fill="none" stroke="#222" stroke-width="1.5"/>
    </svg>
    <p class="study-2">Reduction in intensity of melasma with usage of daily oral Polypodium Leucotomos for 12 weeks with sunscreen SPF 45 (Journal of Clinical Skin Care 2012; 66(4) Page AB21).</p>
  </article>
</section>

</body>
</html>
```